Need Stunning Website for Talent Acquisition (Recruiting) Agency

Hello, I am seeking a very professional, high-quality website that reflects our Talent Acquisition agency, Kindred Hires. Our agency slogan is "Talent Acquisition. Differently." We are in fact different - we are a full service agency that provides services most others do not, and our website needs to immediately reflect that something is different about us when they visit our site.

This contest is to do complete website design and coding, including all graphics, features, plugins, and design elements. The graphics are very important on the site and must be of the highest professional quality. One critical aspect is that the imagery must convey that we serve clients in a variety of industries, including business, healthcare, churches and religious organizations, non-profits, manufacturing, retail, and more. We recruit for both professional level positions (e.g. CEO, COO, Pastor), as well as entry level (e.g. secretary, caregiver, factory worker).
The following pages should be designed:
Home Page - a captivating home page that immediately tells our brand story, what makes us different, and the value that we bring to the table.
Client Services Page - a page that talks more about the services we provide and why we produce better results. This page will cover the 5 C's in greater detail as well as all the things that make us different.
Industries - The industries we serve
Request Services - a page where clients can submit details about a job they would like us to recruit for, including attaching a job description if they have one
Candidates Page - a simple page that encourages prospective candidates to submit their resume for review
About Us - Common about us page
Blog - Common blog page
Contact Us - a contact page for general inquiries
The website must be built in an ultra-SEO friendly manner and optimized for speed and performance. As mentioned above, you will be responsible for providing all graphics for the site (copyright compliant).
The website will need to be compatible with Elementor Pro (I have subscription) and Yoast SEO. It needs to be designed on a high-quality wordpress theme that receives regular updates. It also needs instant chat messaging feature. Would like a traditional menu bar at the top of the page (not a fan of menu's that are hidden or put on the side of the page).

Please, please, please - - do NOT waste my time with generic/stock templates, low-quality graphics, etc. We are a PREMIUM agency and our website needs to reflect that.

In the future we will add a job board - I do not want that initially - but will want the option to add it later.

Must also have the ability to upload documents /attachments on the contact page/form.

It probably goes without saying, but the page must be fully responsive - suitable to work on all device types.

Target Market(s)

Businesses

Industry/Entity Type

Talent Acquisition (Recruiting) Agency

Coding

Coded - Design and coding required

Number of Pages Required

5+ page

Requirements
Must have
• Please see brief
Should not have
• No generic template/stock website or graphics - must have PREMIUM feel.

```html
<!DOCTYPE html>
<html lang="en">
<head>
<meta charset="utf-8">
<title>Kindred Hires — Talent Acquisition</title>
<link href="https://fonts.googleapis.com/css2?family=Poppins:wght@400;500;600;700;800&display=swap" rel="stylesheet">
<style>
:root{
  --navy:#1b2253;
  --orange:#fca60b;
  --ink:#1b2253;
  --text:#4a4f6a;
  --muted:#8a8fa6;
  --hero-bg:#f4f4f5;
  --white:#ffffff;
  --line:#e7e8ee;
}
*{box-sizing:border-box;margin:0;padding:0}
html,body{width:1200px;height:4001px;overflow:hidden}
body{font-family:'Poppins',sans-serif;color:var(--text);background:var(--white);position:relative}
.abs{position:absolute}
a{color:inherit;text-decoration:none}

.site-header{position:absolute;left:0;top:0;width:1200px;height:75px;background:var(--white)}
.brand{position:absolute;left:88px;top:20px}
.brand-name{font-weight:800;font-size:30px;line-height:34px;color:var(--navy);letter-spacing:-.5px;white-space:nowrap}
.main-nav{position:absolute;left:372px;top:28px;display:flex;gap:24px;font-size:14px;font-weight:600;color:var(--ink)}
.sign-in{position:absolute;left:928px;top:29px;font-size:13px;font-weight:600;color:#b8bbc8}
.btn-signup{position:absolute;left:993px;top:22px;width:117px;height:35px;border:2px solid var(--orange);border-radius:4px;font-size:13px;font-weight:700;color:var(--ink);display:flex;align-items:center;justify-content:center}

.hero{position:absolute;left:0;top:75px;width:1200px;height:616px;background:var(--hero-bg)}
.hero-title{position:absolute;left:89px;top:172px;font-size:51px;line-height:58px;font-weight:800;color:var(--ink)}
.hero-sub{position:absolute;left:89px;top:291px;width:420px;font-size:16px;line-height:22px;color:var(--text)}
.search-card{position:absolute;left:90px;top:355px;width:475px;height:96px;background:var(--white);border-radius:8px;box-shadow:0 8px 24px rgba(27,34,83,.08)}
.field{position:absolute;top:30px}
.field b{display:block;font-size:13px;font-weight:600;color:var(--ink)}
.field span{font-size:13px;color:var(--muted)}
.field .chev{position:absolute;top:16px;font-size:10px;color:var(--muted)}
.btn-explore{position:absolute;left:345px;top:23px;width:102px;height:50px;background:var(--orange);border-radius:6px;color:var(--white);font-size:13px;font-weight:700;display:flex;align-items:center;justify-content:center}
.orbit{position:absolute;left:680px;top:57px;width:420px;height:470px}
.chip{position:absolute;background:var(--white);border-radius:6px;box-shadow:0 6px 18px rgba(27,34,83,.1);font-size:10px;font-weight:600;color:var(--ink);padding:6px 12px}
.avatar{position:absolute;border-radius:50%;border:4px solid var(--white);box-shadow:0 4px 12px rgba(27,34,83,.15)}

.stat{position:absolute;top:760px;display:flex;align-items:center;gap:18px}
.stat-icon{width:85px;height:85px;border-radius:14px;display:flex;align-items:center;justify-content:center}
.stat-icon.navy{background:var(--navy)}
.stat-icon.orange{background:var(--orange)}
.stat b{display:block;font-size:34px;line-height:38px;font-weight:800;color:var(--ink)}
.stat span{font-size:16px;color:var(--text)}

.float-card{position:absolute;background:var(--white);border-radius:6px;box-shadow:0 8px 24px rgba(27,34,83,.1)}
.person-name{font-size:13px;color:var(--ink);font-weight:500}
.person-loc{font-size:9px;color:var(--muted)}
.meta{font-size:9px;color:var(--muted)}
.about-text{position:absolute;left:694px;top:995px;width:380px}
.about-text h2{font-size:29px;font-weight:800;color:var(--ink);line-height:34px}
.about-text h3{font-size:42px;font-weight:800;color:var(--ink);line-height:48px}
.about-text h3 em{font-style:normal;color:var(--orange)}
.about-text p{font-size:16px;line-height:22.5px;margin-top:18px;color:var(--text)}

.section-title{position:absolute;left:0;width:1200px;text-align:center;font-weight:800;color:var(--ink)}
.section-sub{position:absolute;left:0;width:1200px;text-align:center;font-size:16px;color:var(--text)}
.band{position:absolute;left:0;top:1724px;width:1200px;height:477px;background:linear-gradient(100deg,#2a3470 0%,var(--navy) 55%,#1d2558 100%)}
.cat-card{position:absolute;top:1592px;width:211px;height:210px;background:var(--white);border-radius:8px;box-shadow:0 10px 28px rgba(27,34,83,.12);padding:36px 33px}
.cat-card.active{background:var(--orange)}
.cat-card h4{font-size:19px;font-weight:700;color:var(--ink);margin-top:26px}
.cat-card p{font-size:15px;line-height:20px;color:var(--text)}
.cat-card.active h4,.cat-card.active p{color:var(--white)}
.cta-title{position:absolute;left:0;top:1905px;width:1200px;text-align:center;font-size:44px;font-weight:800;color:var(--white)}
.cta-sub{position:absolute;left:370px;top:1966px;width:460px;text-align:center;font-size:16px;line-height:22px;color:var(--white)}
.btn-white{position:absolute;left:528px;top:2029px;width:145px;height:52px;background:var(--white);border-radius:6px;color:var(--ink);font-weight:700;font-size:14px;display:flex;align-items:center;justify-content:center}

.cand-title{position:absolute;left:84px;top:2438px;font-size:46px;font-weight:800;color:var(--ink)}
.cand-text{position:absolute;left:84px;top:2506px;width:380px;font-size:16px;line-height:22.5px;color:var(--text)}
.btn-orange{position:absolute;background:var(--orange);color:var(--white);font-weight:700;border-radius:6px;display:flex;align-items:center;justify-content:center}
.photo{position:absolute;border-radius:2px}

.blog-card{position:absolute;top:2966px;width:265px;height:355px;background:var(--white);border-radius:16px;box-shadow:0 10px 28px rgba(27,34,83,.1);overflow:hidden}
.blog-card .photo{left:0;top:0;width:265px;height:209px;border-radius:0}
.blog-body{position:absolute;left:24px;top:226px;right:20px}
.blog-date{font-size:10px;color:var(--text)}
.blog-body h5{font-size:19px;font-weight:700;color:var(--ink);margin-top:2px}
.blog-body p{font-size:11px;line-height:18px;color:var(--text)}
.read-more{font-size:12px;font-weight:700;color:var(--orange);margin-top:4px;display:block}

.footer{position:absolute;left:0;top:3512px;width:1200px;height:489px;background:var(--navy)}
.newsletter{position:absolute;left:175px;top:3414px;width:850px;height:153px;background:var(--orange);border-radius:12px;overflow:hidden}
.newsletter h3{position:absolute;left:47px;top:38px;font-size:33px;font-weight:800;color:var(--white)}
.newsletter p{position:absolute;left:47px;top:85px;width:370px;font-size:13.5px;line-height:19px;color:var(--white)}
.email-field{position:absolute;left:477px;top:50px;width:335px;height:60px;background:var(--white);border-radius:8px}
.email-field span{position:absolute;left:26px;top:19px;font-size:15px;color:var(--text)}
.send{position:absolute;right:10px;top:10px;width:48px;height:40px;border-radius:6px;background:var(--navy);display:flex;align-items:center;justify-content:center}
.foot-brand{position:absolute;left:88px;top:3706px}
.foot-brand .brand-name{color:var(--white);font-size:38px;line-height:42px}
.foot-phone{position:absolute;left:87px;top:3764px;font-size:27px;font-weight:700;color:var(--white)}
.foot-mail{position:absolute;left:87px;top:3801px;font-size:16px;color:var(--white)}
.foot-col{position:absolute;top:3688px;color:var(--white)}
.foot-col h6{font-size:15px;font-weight:700;margin-bottom:6px}
.foot-col li{list-style:none;font-size:12px;line-height:25px;color:#e5e7f2}
.foot-rule{position:absolute;left:88px;top:3937px;width:1024px;height:1px;background:rgba(255,255,255,.25)}
.copyright{position:absolute;left:0;top:3956px;width:1200px;text-align:center;font-size:15px;color:var(--white)}
.chat{position:absolute;left:1107px;top:3900px;width:57px;height:57px;border-radius:50%;background:var(--orange);display:flex;align-items:center;justify-content:center}
</style>
</head>
<body>

<header class="site-header">
  <div class="brand"><div class="brand-name">Kindred Hires</div></div>
  <nav class="main-nav">
    <a>Client Service</a><a>Industries</a><a>Candidates</a><a>About</a><a>Blog</a><a>Contact</a>
  </nav>
  <a class="sign-in">SIGN IN</a>
  <a class="btn-signup">SIGN UP</a>
</header>

<section class="hero">
  <h1 class="hero-title">It's Easy to Find<br>Your Dream Job</h1>
  <p class="hero-sub">Explore thousands of jobs in one place and get the job of your dream.</p>
  <div class="search-card">
    <div class="field" style="left:26px"><b>Select Job Type</b><span>Healthcare</span><i class="chev" style="left:155px">⌄</i></div>
    <div class="field" style="left:203px"><b>Location</b><span>Los Angles</span><i class="chev" style="left:100px">⌄</i></div>
    <a class="btn-explore">EXPLORE</a>
  </div>

  <div class="orbit">
    <svg class="abs" style="left:10px;top:100px" width="400" height="360" viewBox="0 0 400 360">
      <ellipse cx="200" cy="190" rx="195" ry="165" fill="none" stroke="#c8cad4" stroke-width="1.5" stroke-dasharray="5 5"/>
    </svg>
    <div class="abs" role="img" aria-label="Smiling professional woman holding a laptop" style="left:105px;top:0;width:230px;height:400px;border-radius:115px 115px 0 0;background:linear-gradient(180deg,#e9e6e2 0%,#cfcbc6 55%,#f1c11f 100%)"></div>
    <div class="avatar" role="img" aria-label="Portrait of a candidate" style="left:29px;top:88px;width:56px;height:56px;background:linear-gradient(#f6b400,#e49300)"></div>
    <div class="avatar" role="img" aria-label="Portrait of a candidate" style="left:334px;top:122px;width:74px;height:74px;background:linear-gradient(#5fc3e8,#2e9dc8)"></div>
    <div class="avatar" role="img" aria-label="Portrait of a candidate" style="left:306px;top:406px;width:52px;height:52px;background:linear-gradient(#67b7f0,#3a88c9)"></div>
    <svg class="abs" style="left:67px;top:127px" width="20" height="20"><circle cx="10" cy="10" r="9" fill="#22c27a"/><path d="M6 10l3 3 5-6" stroke="#fff" stroke-width="2" fill="none"/></svg>
    <svg class="abs" style="left:390px;top:180px" width="20" height="20"><circle cx="10" cy="10" r="9" fill="#f25a2a"/><circle cx="10" cy="10" r="3" fill="#fff"/></svg>
    <svg class="abs" style="left:343px;top:444px" width="20" height="20"><circle cx="10" cy="10" r="9" fill="#22c27a"/><path d="M6 10l3 3 5-6" stroke="#fff" stroke-width="2" fill="none"/></svg>
    <div class="chip" style="left:99px;top:118px;font-size:9px">Churches</div>
    <div class="chip" style="left:260px;top:214px">Manufacturing</div>
    <div class="chip" style="left:276px;top:287px;width:110px;height:46px;padding:8px 10px 0 52px;line-height:11px">Religious organizations
      <span class="abs" style="left:14px;top:12px;width:22px;height:22px;border-radius:5px;background:var(--navy)"></span></div>
    <div class="chip" style="left:-26px;top:357px;width:158px;height:75px;padding:10px 14px 0 60px;font-size:12px">Healthcare<br><span style="font-size:9px;color:var(--muted);font-weight:400">Brightpath</span>
      <span class="abs" style="left:16px;top:12px;width:30px;height:30px;border-radius:50%;border:1px solid var(--line)"></span>
      <span class="abs" style="left:12px;top:53px;font-size:8px;color:#f25a2a">You were invited</span></div>
    <div class="chip" style="left:160px;top:433px">Non-profits</div>
  </div>
</section>

<section class="stats">
  <div class="stat" style="left:168px">
    <div class="stat-icon navy"><svg width="40" height="36" viewBox="0 0 40 36" fill="none" stroke="#fff" stroke-width="2.6"><rect x="3" y="9" width="34" height="24" rx="3"/><path d="M14 9V4h12v5M3 19h34M20 16v6"/></svg></div>
    <div><b>50k+</b><span>Job Vacancy</span></div>
  </div>
  <div class="stat" style="left:501px">
    <div class="stat-icon orange"><svg width="36" height="38" viewBox="0 0 36 38" fill="none" stroke="#fff" stroke-width="2.6"><circle cx="18" cy="11" r="8"/><path d="M3 36c0-9 7-14 15-14s15 5 15 14"/></svg></div>
    <div><b>20k+</b><span>People Got Hired</span></div>
  </div>
  <div class="stat" style="left:815px">
    <div class="stat-icon navy"><svg width="40" height="40" viewBox="0 0 40 40" fill="none" stroke="#fff" stroke-width="2.4"><path d="M6 36V4h18v32M6 36h20M11 10h3M17 10h2M11 16h3M17 16h2M11 22h3M17 22h2"/><circle cx="30" cy="24" r="6"/><path d="M30 30l0 6"/></svg></div>
    <div><b>2k+</b><span>Companies</span></div>
  </div>
</section>

<section class="about">
  <div class="photo" role="img" aria-label="Woman in a yellow jacket working on a laptop in an office" style="left:160px;top:947px;width:455px;height:408px;background:linear-gradient(120deg,#7b7e84 0%,#b9b7b1 40%,#d79a18 70%,#8d8a84 100%)"></div>
  <div class="float-card" style="left:228px;top:938px;width:192px;height:82px">
    <span class="abs" style="left:14px;top:12px;width:30px;height:30px;border-radius:50%;background:#c9b5ef"></span>
    <div class="abs" style="left:54px;top:12px"><div class="person-name">Omar Velic</div><div class="person-loc">Ankara, Turkey</div></div>
    <div class="abs meta" style="left:14px;top:58px">☰ 2 Notes</div>
    <div class="abs meta" style="left:96px;top:58px">▯ via Folio</div>
  </div>
  <div class="float-card" style="left:78px;top:1042px;width:192px;height:92px">
    <span class="abs" style="left:14px;top:14px;width:30px;height:30px;border-radius:50%;background:#bfe8c7"></span>
    <div class="abs" style="left:54px;top:14px"><div class="person-name">Clara Whitfield</div><div class="person-loc">London, United Kingdom</div></div>
    <div class="abs meta" style="left:14px;top:66px">☰ 3 Notes</div>
    <div class="abs meta" style="left:100px;top:66px">▯ via Social</div>
  </div>
  <div class="float-card" style="left:87px;top:1189px;width:252px;height:178px">
    <div class="abs" style="left:16px;top:14px;font-size:13px;color:var(--ink)">▮ Platform Performance</div>
    <div class="abs" style="left:16px;top:44px;font-size:26px;color:var(--ink)">2,173</div>
    <div class="abs" style="left:92px;top:56px;font-size:10px;background:#d4f5df;color:#1aa45a;border-radius:8px;padding:0 7px">+12</div>
    <svg class="abs" style="left:14px;top:90px" width="224" height="76" viewBox="0 0 224 76">
      <g fill="#1e3ee6">
        <rect x="2" y="66" width="4" height="8" rx="2"/><rect x="14" y="60" width="4" height="14" rx="2"/><rect x="26" y="56" width="4" height="18" rx="2"/><rect x="38" y="50" width="4" height="24" rx="2"/><rect x="50" y="56" width="4" height="18" rx="2"/><rect x="62" y="44" width="4" height="30" rx="2"/><rect x="74" y="28" width="4" height="46" rx="2"/><rect x="86" y="40" width="4" height="34" rx="2"/><rect x="98" y="20" width="4" height="54" rx="2"/><rect x="110" y="48" width="4" height="26" rx="2"/><rect x="122" y="66" width="4" height="8" rx="2"/><rect x="134" y="4" width="4" height="70" rx="2"/><rect x="146" y="40" width="4" height="34" rx="2"/><rect x="158" y="30" width="4" height="44" rx="2"/><rect x="170" y="22" width="4" height="52" rx="2"/><rect x="182" y="38" width="4" height="36" rx="2"/><rect x="194" y="14" width="4" height="60" rx="2"/><rect x="206" y="12" width="4" height="62" rx="2"/>
      </g>
    </svg>
  </div>
  <div class="about-text">
    <h2>About us</h2>
    <h3>Kindred <em>Hires</em></h3>
    <p>Lorem Ipsum is simply dummy text of the printing and typesetting industry. Lorem Ipsum has been the industry's standard dummy text ever since the 1500s, when an unknown printer took a galley of type and scrambled it to make a type specimen book. It has survived not only five centuries, but also the leap i.</p>
  </div>
</section>

<section class="categories">
  <h2 class="section-title" style="top:1478px;font-size:44px">Browse Job Categories</h2>
  <p class="section-sub" style="top:1541px">Many Categories will make your searching easier</p>
  <div class="band" role="img" aria-label="Team collaborating in a modern office, tinted navy"></div>

  <div class="cat-card" style="left:159px">
    <svg width="52" height="48" viewBox="0 0 52 48" fill="var(--orange)"><path d="M26 46L6 26C-2 18 4 4 15 5c5 0 8 3 11 7 3-4 6-7 11-7 11-1 17 13 9 21z"/><path d="M12 24l10 10M18 20l10 10M24 16l10 10" stroke="#fff" stroke-width="2.5"/></svg>
    <h4>Non-profits</h4><p>100+ New Job<br>Posted</p>
  </div>
  <div class="cat-card" style="left:382px">
    <svg width="52" height="50" viewBox="0 0 52 50" fill="var(--orange)"><path d="M2 48V6h7v20l12-8v8l12-8v8l12-8v30z"/><g fill="#fff"><rect x="10" y="36" width="4" height="4"/><rect x="18" y="36" width="4" height="4"/><rect x="26" y="36" width="4" height="4"/><rect x="34" y="36" width="4" height="4"/><rect x="42" y="36" width="4" height="4"/></g></svg>
    <h4>Manufacturing</h4><p>100+ New Job<br>Posted</p>
  </div>
  <div class="cat-card active" style="left:606px">
    <svg width="52" height="48" viewBox="0 0 52 48" fill="#fff"><path d="M26 46L6 26C-2 18 4 4 15 5c5 0 8 3 11 7 3-4 6-7 11-7 11-1 17 13 9 21z"/><path d="M28 18h8v8h8v8h-8v8h-8v-8h-8v-8h8z" fill="#fff" stroke="var(--orange)" stroke-width="2"/></svg>
    <h4>Healthcare</h4><p>100+ New Job<br>Posted</p>
  </div>
  <div class="cat-card" style="left:831px">
    <svg width="52" height="52" viewBox="0 0 52 52" fill="var(--orange)"><path d="M24 2h4v7h6v4h-6v7h-4v-7h-6V9h6z"/><path d="M26 20L4 36h5v14h12V40a5 5 0 0110 0v10h12V36h5z"/></svg>
    <h4>Churches</h4><p>100+ New Job<br>Posted</p>
  </div>

  <h2 class="cta-title">Get your Job Now!</h2>
  <p class="cta-sub">Start your journey with other applicants and make your dream come true.</p>
  <a class="btn-white">SIGN IN</a>
</section>

<section class="candidates">
  <h2 class="cand-title">Candidates</h2>
  <p class="cand-text">Lorem Ipsum is simply dummy text of the printing and typesetting industry. Lorem Ipsum has been the industry's standard dummy text ever since the 1500s, when an unknown printer took a galley of type and scrambled it to make a type specimen book. It has survived not only five centuries, but also the leap i.</p>
  <a class="btn-orange" style="left:84px;top:2672px;width:145px;height:52px;font-size:14px">APPLY NOW</a>

  <div class="photo" role="img" aria-label="Two colleagues reviewing work together at a desk" style="left:573px;top:2378px;width:228px;height:322px;background:linear-gradient(160deg,#eeeeec 0%,#c9c6bf 50%,#e2b63c 85%,#8c8a86 100%)"></div>
  <div class="photo" role="img" aria-label="Woman working on a laptop at home" style="left:830px;top:2312px;width:228px;height:215px;background:linear-gradient(150deg,#d9d7d2 0%,#6e6a63 55%,#2c2b2a 100%)"></div>
  <div class="photo" role="img" aria-label="Woman smiling at her laptop in a kitchen" style="left:830px;top:2558px;width:228px;height:214px;background:linear-gradient(160deg,#e9e6e1 0%,#c3b8aa 50%,#a27c58 100%)"></div>
  <div class="float-card" style="left:928px;top:2429px;width:233px;height:67px">
    <span class="abs" style="left:16px;top:14px;width:40px;height:40px;border-radius:6px;background:#fff1d6"></span>
    <svg class="abs" style="left:26px;top:26px" width="20" height="16" fill="none" stroke="var(--orange)" stroke-width="1.8"><rect x="1" y="1" width="18" height="14" rx="2"/><path d="M1 2l9 7 9-7"/></svg>
    <div class="abs" style="left:80px;top:17px;font-size:12px;line-height:15px;color:var(--ink)">Work Inquiry From<br><b style="font-weight:600">Kindred Hires</b></div>
  </div>
  <div class="float-card" style="left:622px;top:2620px;width:244px;height:127px">
    <div class="abs" style="left:0;top:22px;width:244px;text-align:center;font-size:13px;color:var(--ink)">10k+ Candidates</div>
    <span class="abs" style="left:30px;top:60px;width:42px;height:42px;border-radius:50%;background:#2d4a3c;border:2px solid #fff"></span>
    <span class="abs" style="left:64px;top:60px;width:42px;height:42px;border-radius:50%;background:#b99a7e;border:2px solid #fff"></span>
    <span class="abs" style="left:98px;top:60px;width:42px;height:42px;border-radius:50%;background:#6a4a35;border:2px solid #fff"></span>
    <span class="abs" style="left:132px;top:60px;width:42px;height:42px;border-radius:50%;background:#8aa3bb;border:2px solid #fff"></span>
    <span class="abs" style="left:166px;top:64px;width:34px;height:34px;border-radius:50%;background:#f0f1f5;text-align:center;line-height:34px;font-size:18px;color:var(--ink)">+</span>
  </div>
</section>

<section class="blog">
  <h2 class="section-title" style="top:2880px;font-size:44px">Latest Blog</h2>
  <article class="blog-card" style="left:185px">
    <div class="photo" role="img" aria-label="Man with a laptop in an office" style="background:linear-gradient(160deg,#dcdad5,#8b877e 60%,#4d4a42)"></div>
    <div class="blog-body"><div class="blog-date">06/ May/ 2022</div><h5>Heading here</h5><p>Lorem Ipsum has been the industry's standard dummy text ever since.</p><a class="read-more">READ MORE</a></div>
  </article>
  <article class="blog-card" style="left:467px">
    <div class="photo" role="img" aria-label="Two colleagues laughing together" style="background:linear-gradient(160deg,#5e7086,#c8b6a0 55%,#e9e6e0)"></div>
    <div class="blog-body"><div class="blog-date">06/ May/ 2022</div><h5>Heading here</h5><p>Lorem Ipsum has been the industry's standard dummy text ever since.</p><a class="read-more">READ MORE</a></div>
  </article>
  <article class="blog-card" style="left:750px">
    <div class="photo" role="img" aria-label="Team meeting around a table" style="background:linear-gradient(160deg,#d9dde0,#8d98a3 55%,#5b6470)"></div>
    <div class="blog-body"><div class="blog-date">06/ May/ 2022</div><h5>Heading here</h5><p>Lorem Ipsum has been the industry's standard dummy text ever since.</p><a class="read-more">READ MORE</a></div>
  </article>
</section>

<footer class="footer"></footer>
<div class="newsletter">
  <svg class="abs" style="left:0;top:0" width="850" height="153" fill="none" stroke="rgba(255,255,255,.25)" stroke-width="1">
    <path d="M330 0L570 90L700 20L850 70M570 90L610 153M700 20L720 0M560 0L570 90M440 153L570 90"/>
  </svg>
  <h3>Let employers find you</h3>
  <p>Advertise your jobs to millions of monthly users and search 15.8 million CVs in our database.</p>
  <div class="email-field"><span>Email Address</span>
    <div class="send"><svg width="16" height="16" viewBox="0 0 16 16" fill="#fff"><path d="M15 1L1 7l5 2 2 6z"/></svg></div>
  </div>
</div>

<div class="foot-brand"><div class="brand-name">Kindred Hires</div></div>
<div class="foot-phone">555 010 2468</div>
<div class="foot-mail">support@KindredHires.com</div>

<div class="foot-col" style="left:410px"><h6>For Candidates</h6><ul><li>Browse Jobs</li><li>Browse Candidates</li><li>Candidate Dashboard</li><li>Job Alerts</li><li>My Bookmarks</li></ul></div>
<div class="foot-col" style="left:613px"><h6>For Employers</h6><ul><li>All Employers</li><li>Employer Dashboard</li><li>Submit Job</li><li>Job Packages</li></ul></div>
<div class="foot-col" style="left:812px"><h6>About Us</h6><ul><li>Contact Us</li><li>About Us</li><li>Terms</li><li>Packages</li><li>FAQ</li></ul></div>
<div class="foot-col" style="left:962px"><h6>Helpful Resources</h6><ul><li>Site Map</li><li>Terms of Use</li><li>Privacy Center</li><li>Security Center</li><li>Accessibility Center</li></ul></div>

<div class="foot-rule"></div>
<div class="copyright">©Copyright 2022 | All Rights Reserved</div>
<a class="chat" aria-label="Open chat"><svg width="28" height="26" viewBox="0 0 28 26" fill="#fff"><path d="M14 2C7 2 2 6.5 2 12c0 3 1.5 5.6 4 7.4L5 24l5.5-3c1.1.3 2.3.5 3.5.5 7 0 12-4.5 12-10S21 2 14 2z"/></svg></a>

</body>
</html>
```